I'm a family owned and operated electrical contractor in Colorado USA. We offer a full electrical service, remodel and new construction, we also offer energy saving solutions like LED lighting, photo voltaic, and wind energy,
We sell and install BrightNova light fixtures (rbightNova.com)
More information about my business can be looked at my website copperpeakelcetric.com My logo is on my website.

Industry/Entity Type

Electrical

Contact Information for Business Card

Copper Peak Electric, Dwight Sorensby, Owner, BrightNova Sale & Install, Full Electrical Service, Remodel & New Construction. P: 303-512-8847 F:303-264-3318 E:dwight@copperpeakelectric.com, 27519 CR41, Ridgeford, WY 80194

```html
<!DOCTYPE html>
<html lang="en">
<head>
<meta charset="utf-8">
<title>Copper Peak Electric — Business Card</title>
<link rel="stylesheet" href="https://fonts.googleapis.com/css2?family=Ubuntu:wght@400;500;700&display=swap">
<style>
  :root {
    --backdrop: #ecebe8;
    --card: #ffffff;
    --band: #434343;
    --band-text: #ffffff;
    --ink: #1d1d1d;
    --leaf: #5cc21a;
    --edge: #d8d8d8;
  }
  * { margin: 0; padding: 0; box-sizing: border-box; }
  html, body {
    width: 1200px;
    height: 900px;
    overflow: hidden;
    background: var(--backdrop);
    font-family: "Ubuntu", sans-serif;
  }
  .canvas { position: relative; width: 1200px; height: 900px; }

  .card {
    position: absolute;
    left: 339px;
    width: 548px;
    height: 296px;
    background: var(--card);
    border: 1px solid var(--edge);
    border-radius: 9px;
    overflow: hidden;
  }
  .card--front { top: 118px; }
  .card--back  { top: 451px; }

  .band {
    position: absolute;
    background: var(--band);
    color: var(--band-text);
  }

  /* front */
  .services {
    left: 0;
    top: 87px;
    width: 271px;
    height: 106px;
    padding: 24px 10px 0 0;
    text-align: right;
    font-size: 15px;
    font-weight: 500;
    line-height: 22px;
    letter-spacing: 0.2px;
  }
  .brand {
    position: absolute;
    display: flex;
    align-items: center;
    gap: 8px;
    color: var(--ink);
    font-weight: 700;
    text-transform: uppercase;
    white-space: nowrap;
  }
  .brand__dot {
    border-radius: 50%;
    background: var(--leaf);
    flex: none;
  }
  .brand--front { left: 296px; top: 94px; font-size: 17px; }
  .brand--front .brand__dot { width: 20px; height: 20px; }

  /* back */
  .brand--back { left: 283px; top: 22px; font-size: 14px; }
  .brand--back .brand__dot { width: 16px; height: 16px; }

  .contact-strip {
    left: 0;
    top: 109px;
    width: 100%;
    height: 106px;
  }
  .person {
    position: absolute;
    left: 41px;
    top: 12px;
    font-size: 15px;
    font-weight: 500;
    line-height: 20px;
    letter-spacing: 0.2px;
  }
  .details {
    position: absolute;
    left: 286px;
    top: 12px;
    font-size: 13.5px;
    line-height: 25px;
    letter-spacing: 0.1px;
    list-style: none;
    white-space: nowrap;
  }
</style>
</head>
<body>
<main class="canvas">

  <section class="card card--front" aria-label="Card front">
    <div class="band services">
      <p>BrightNova Sale &amp; Install</p>
      <p>Full Electrical Service</p>
      <p>Remodel &amp; New Construction</p>
    </div>
    <div class="brand brand--front">
      <span class="brand__dot" aria-hidden="true"></span>
      <span>Copper Peak Electric</span>
    </div>
  </section>

  <section class="card card--back" aria-label="Card back">
    <div class="brand brand--back">
      <span class="brand__dot" aria-hidden="true"></span>
      <span>Copper Peak Electric</span>
    </div>
    <div class="band contact-strip">
      <div class="person">
        <p>Dwight Sorensby</p>
        <p>Owner</p>
      </div>
      <ul class="details">
        <li>P: 303-512-8847 F:303-264-3318</li>
        <li>E:dwight@copperpeakelectric.com,</li>
        <li>27519 CR41, Ridgeford, WY 80194</li>
      </ul>
    </div>
  </section>

</main>
</body>
</html>
```